Torvelin Business Card

We need a business card design. We have a logo from a previous PixelHarbor project and I am attaching the logo files in jpeg and photoshop.

Business

```html
<!DOCTYPE html>
<html lang="en">
<head>
<meta charset="utf-8">
<title>Torvelin Business Card</title>
<link rel="stylesheet" href="https://fonts.googleapis.com/css2?family=Poppins:wght@400;600&display=swap">
<style>
  :root {
    --page-bg: #eeeff0;
    --card-bg: #ffffff;
    --card-fade: #f1f2f2;
    --ink-dark: #2b2b2b;
    --ink-mid: #3a3a3a;
    --brand-green: #3cb54a;
    --brand-green-deep: #2e9a3c;
    --band-dark: #1f2224;
    --band-dark-edge: #2c3033;
  }
  * { box-sizing: border-box; margin: 0; padding: 0; }
  html, body {
    width: 1200px;
    height: 900px;
    overflow: hidden;
    background: var(--page-bg);
    font-family: "Poppins", sans-serif;
  }
  .stage {
    width: 1200px;
    height: 900px;
    display: flex;
    align-items: center;
    justify-content: center;
  }
  .business-card {
    position: relative;
    width: 1000px;
    height: 572px;
    border-radius: 34px;
    overflow: hidden;
    background: linear-gradient(160deg, var(--card-bg) 0%, var(--card-bg) 45%, var(--card-fade) 100%);
    box-shadow: 0 18px 40px rgba(0, 0, 0, 0.12);
  }
  .brand {
    position: absolute;
    left: 64px;
    top: 60px;
    display: flex;
    align-items: center;
    gap: 22px;
  }
  .brand-square {
    width: 66px;
    height: 66px;
    background: var(--brand-green);
  }
  .brand-name {
    font-size: 72px;
    font-weight: 600;
    line-height: 1;
    letter-spacing: -1px;
    color: var(--ink-dark);
  }
  .person {
    position: absolute;
    left: 64px;
    top: 190px;
  }
  .person-name {
    font-size: 32px;
    font-weight: 600;
    color: var(--ink-dark);
    line-height: 1.2;
  }
  .person-role {
    font-size: 22px;
    font-weight: 400;
    color: var(--ink-mid);
    line-height: 1.3;
  }
  .contact-list {
    position: absolute;
    left: 64px;
    top: 300px;
    list-style: none;
  }
  .contact-item {
    display: flex;
    align-items: center;
    gap: 14px;
    height: 40px;
    font-size: 26px;
    line-height: 1;
    color: var(--ink-dark);
  }
  .contact-icon {
    width: 30px;
    height: 30px;
    flex: none;
    fill: var(--brand-green);
  }
  .contact-item--indent { padding-left: 44px; }
  .card-band {
    position: absolute;
    left: 0;
    right: 0;
    bottom: 0;
    height: 80px;
  }
  .card-band-stripe {
    height: 12px;
    background: linear-gradient(90deg, var(--brand-green-deep), var(--brand-green));
  }
  .card-band-base {
    height: 68px;
    background: linear-gradient(180deg, var(--band-dark-edge), var(--band-dark));
  }
</style>
</head>
<body>
<main class="stage">
  <article class="business-card">
    <header class="brand">
      <span class="brand-square"></span>
      <span class="brand-name">Torvelin</span>
    </header>

    <section class="person">
      <p class="person-name">Marlo Venn</p>
      <p class="person-role">Manager</p>
    </section>

    <ul class="contact-list">
      <li class="contact-item">
        <svg class="contact-icon" viewBox="0 0 24 24" aria-hidden="true">
          <path d="M6.6 10.8a15.1 15.1 0 0 0 6.6 6.6l2.2-2.2a1 1 0 0 1 1-.25 11.4 11.4 0 0 0 3.6.57 1 1 0 0 1 1 1V20a1 1 0 0 1-1 1A17 17 0 0 1 3 4a1 1 0 0 1 1-1h3.5a1 1 0 0 1 1 1c0 1.250.2 2.450.57 3.57a1 1 0 0 1-.25 1z"/>
        </svg>
        <span>1800-522-7304</span>
      </li>
      <li class="contact-item">
        <svg class="contact-icon" viewBox="0 0 24 24" aria-hidden="true">
          <path d="M3 5h18a1 1 0 0 1 1 1v12a1 1 0 0 1-1 1H3a1 1 0 0 1-1-1V6a1 1 0 0 1 1-1zm1 2.2V17h16V7.2l-8 5.3z M4.6 7 12 11.9 19.4 7z"/>
        </svg>
        <span>info@torvelin.com</span>
      </li>
      <li class="contact-item">
        <svg class="contact-icon" viewBox="0 0 24 24" aria-hidden="true">
          <path d="M12 3 2 11.5h3V21h5.5v-6h3v6H19v-9.5h3z"/>
        </svg>
        <span>2715 Harlow Ave. Suite 410</span>
      </li>
      <li class="contact-item contact-item--indent">
        <span>Crestport, FL 32019</span>
      </li>
    </ul>

    <footer class="card-band">
      <div class="card-band-stripe"></div>
      <div class="card-band-base"></div>
    </footer>
  </article>
</main>
</body>
</html>
```